Business card design for a Cloud Service Provider Company

We already have business card and would like to update and get a different design. Our company is Managed IT services and Cloud Solutions Company, Dorlen Systems. Attached is our current logo, current business card and sample design. I am not sure if we still need to keep our partners details on the back of the card as it does not look good to me... Please let me know if you need any additional information...

Target Market(s)

Any verticals with IT infrastructure - CEOs, CFOs and CIOs

Industry/Entity Type

Information Technology

Requirements
Must have
• First Name Last Name
• Phone
• Email address
• Company Logo

```html
<!DOCTYPE html>
<html lang="en">
<head>
<meta charset="utf-8">
<title>Dorlen Systems – Business Card</title>
<link href="https://fonts.googleapis.com/css2?family=Arimo:wght@400;700&display=swap" rel="stylesheet">
<style>
  :root {
    --stage-light: #e4e4e4;
    --stage-dark: #7a7a7a;
    --brand-blue: #139fdc;
    --brand-blue-deep: #0a8ccc;
    --brand-green: #9bd23c;
    --card-white: #ffffff;
    --ink: #1e1e1e;
    --ink-soft: #3a3a3a;
  }
  * { box-sizing: border-box; margin: 0; padding: 0; }
  html, body { width: 1200px; height: 960px; overflow: hidden; }
  body {
    font-family: "Arimo", Arial, sans-serif;
    background: radial-gradient(ellipse at 55% 55%, var(--stage-light) 0%, #b9b9b9 55%, var(--stage-dark) 100%);
    position: relative;
  }
  .brand-headline {
    position: absolute;
    left: 64px; top: 110px;
    display: flex; align-items: center; gap: 22px;
    color: var(--card-white);
    font-size: 92px; font-weight: 700; letter-spacing: -1px;
  }
  .brand-dot {
    width: 34px; height: 34px; border-radius: 50%;
    background: var(--card-white);
  }
  .card {
    position: absolute;
    width: 510px; height: 310px;
    border-radius: 4px;
    box-shadow: 0 14px 30px rgba(0,0,0,.28);
  }
  .card-front {
    left: 50px; top: 400px;
    background: linear-gradient(135deg, var(--brand-blue) 0%, var(--brand-blue-deep) 100%);
    color: var(--card-white);
    display: flex; flex-direction: column; align-items: center; justify-content: center;
  }
  .front-logo {
    display: flex; align-items: center; gap: 14px;
    font-size: 50px; font-weight: 700;
  }
  .front-logo .brand-mark {
    width: 22px; height: 22px; border-radius: 50%;
    background: var(--brand-green);
  }
  .front-tagline {
    margin-top: 14px; font-size: 20px; letter-spacing: .5px;
  }
  .card-back {
    left: 640px; top: 400px;
    background: var(--card-white);
    color: var(--ink);
    padding: 30px 34px;
  }
  .person-name { font-size: 18px; font-weight: 700; }
  .person-role { font-size: 14px; margin-top: 3px; color: var(--ink-soft); }
  .contact-list { margin-top: 20px; font-size: 13.5px; line-height: 1.4; }
  .contact-list b { display: inline-block; width: 16px; }
  .back-logo {
    position: absolute; right: 34px; top: 112px;
    text-align: right;
  }
  .back-logo .logo-name {
    display: flex; align-items: center; gap: 10px; justify-content: flex-end;
    font-size: 32px; font-weight: 700; color: var(--ink);
  }
  .back-logo .brand-mark {
    width: 16px; height: 16px; border-radius: 50%;
    background: var(--brand-blue);
  }
  .back-logo .logo-tagline { font-size: 12px; margin-top: 5px; color: var(--ink-soft); }
  .office-details {
    position: absolute; right: 34px; bottom: 26px;
    text-align: right; font-size: 13.5px; line-height: 1.4;
  }
  .office-details .web { font-weight: 700; }
</style>
</head>
<body>
  <div class="brand-headline"><span>Dorlen Systems</span><span class="brand-dot"></span></div>

  <section class="card card-front" aria-label="Card front">
    <div class="front-logo"><span>Dorlen Systems</span><span class="brand-mark"></span></div>
    <div class="front-tagline">Cloud Service Provider</div>
  </section>

  <section class="card card-back" aria-label="Card back">
    <div class="person-name">Reid T. Calloway</div>
    <div class="person-role">Technical Manager</div>
    <div class="contact-list">
      <div>reid.calloway@dorlen.com.au</div>
      <div><b>p</b>+61 (2) 5550 1015</div>
      <div><b>m</b>+61 (0) 400 555 137</div>
    </div>
    <div class="back-logo">
      <div class="logo-name"><span>Dorlen Systems</span><span class="brand-mark"></span></div>
      <div class="logo-tagline">Cloud Service Provider</div>
    </div>
    <div class="office-details">
      <div>Suite 204, 12 Harlow Lane</div>
      <div>Northfield NSW 2090, Australia</div>
      <div><b>Main</b> +61 (2) 5550 0104</div>
      <div><b>Support</b> 1300 555 400</div>
      <div class="web">www.dorlen.com.au</div>
    </div>
  </section>
</body>
</html>
```